BrivoMatex. Lantern for the Steady Growth. Business card

Professional business card for BrivoMatex (Lantern for the Steady Growth)
My rationale: Strategy-> Execution-> Results-> Value that lead to the BrivoMatex name: We put the Lantern for the Steady Growth.
We deliver value to our customers helping them at defining a good strategy (cyan arrow). 90% of well formulated strategies fail due to poor execution so we also consider strategical execution very important (green arrow). Due to the execution we obtain the results (blue arrow). Finally, the results provide feedback to redefine strategy, and the new strategy has to be executed and new results obtained providing new feedback and on and on. It's like a wheel that finally, must create corporate value: value for shareholders, staholders, employees, providers...-

Target Market(s)

CEOs and steering comitees , invewrnent funds

Industry/Entity Type

Business Consultant

Contact Information for Business Card

Tommaso Ferlini
CEO & Founder
tommaso.ferlini@brivomatex.example
Mobile: +34 611.205.938
www.brivomatex.example

Colors

Designer to choose colors to be used in the design.

Requirements
Nice to have
• Nice to hace the words: Strategy, execution, results
• Nice to vave the claim: Lantern for the Steady Growth
• The three colors should be shown:
• cyan for STRATEGY
• green for EXECUTION
• blue for RESULTS
Should not have
• Complete black background

```html
<!DOCTYPE html>
<html lang="en">
<head>
<meta charset="utf-8">
<title>BrivoMatex – Business Card</title>
<link href="https://fonts.googleapis.com/css2?family=Arimo:wght@400;700&display=swap" rel="stylesheet">
<style>
  :root{
    --brand-blue:#2e3189;
    --brand-cyan:#29abe2;
    --brand-green:#8cc63f;
    --ink:#1f1f2b;
    --paper:#ffffff;
    --backdrop:#5a5d63;
    --backdrop-light:#8d9096;
  }
  *{margin:0;padding:0;box-sizing:border-box}
  html,body{width:1200px;height:766px;overflow:hidden}
  body{
    background:linear-gradient(160deg,var(--backdrop-light),var(--backdrop));
    font-family:"Arimo",Arial,sans-serif;
    position:relative;
  }
  .card{
    position:absolute;top:234px;width:520px;height:298px;
    box-shadow:0 6px 18px rgba(0,0,0,.35);
  }
  /* Front */
  .card-front{left:50px;background:var(--paper);}
  .front-brand{
    position:absolute;left:34px;top:118px;
    display:flex;align-items:center;gap:10px;
  }
  .brand-dot{width:18px;height:18px;border-radius:50%;background:var(--brand-blue)}
  .brand-name{font-weight:700;font-size:30px;color:var(--brand-blue);letter-spacing:-.5px}
  .divider{position:absolute;left:228px;top:70px;width:2px;height:120px;background:var(--brand-green)}
  .contact{position:absolute;left:252px;top:62px}
  .person-name{font-weight:700;font-size:22px;color:var(--brand-blue)}
  .person-name .surname{color:var(--brand-cyan)}
  .person-title{font-size:13px;color:var(--ink);margin-top:4px}
  .contact-list{list-style:none;margin-top:14px}
  .contact-list li{display:flex;align-items:center;gap:8px;font-size:12.5px;color:var(--ink);margin-bottom:5px}
  .contact-list svg{width:12px;height:12px;flex:none}
  .pillars{
    position:absolute;left:252px;bottom:40px;
    font-weight:700;font-size:14px;letter-spacing:.5px;
  }
  .pillar-strategy{color:var(--brand-cyan)}
  .pillar-execution{color:var(--brand-green)}
  .pillar-results{color:var(--brand-blue)}
  /* Back */
  .card-back{left:630px;background:var(--brand-blue);color:var(--paper);
    display:flex;flex-direction:column;align-items:center;justify-content:center}
  .back-brand{display:flex;align-items:center;gap:14px}
  .back-brand .brand-dot{width:26px;height:26px;background:var(--paper)}
  .back-brand .brand-name{font-size:48px;color:var(--paper)}
  .claim{font-size:15px;margin-top:14px}
</style>
</head>
<body>
  <section class="card card-front" aria-label="Business card front">
    <div class="front-brand">
      <span class="brand-dot"></span>
      <span class="brand-name">BrivoMatex</span>
    </div>
    <div class="divider"></div>
    <div class="contact">
      <div class="person-name">Tommaso <span class="surname">Ferlini</span></div>
      <div class="person-title">CEO &amp; Founder</div>
      <ul class="contact-list">
        <li>
          <svg viewBox="0 0 12 12"><rect x="2.5" y="0.5" width="7" height="11" rx="1" fill="none" stroke="#1f1f2b"/></svg>
          +34 611.205.938
        </li>
        <li>
          <svg viewBox="0 0 12 12"><rect x="0.5" y="2" width="11" height="8" fill="none" stroke="#1f1f2b"/><path d="M0.5 2 L6 7 L11.5 2" fill="none" stroke="#1f1f2b"/></svg>
          tommaso.ferlini@brivomatex.example
        </li>
        <li>
          <svg viewBox="0 0 12 12"><circle cx="6" cy="6" r="5.5" fill="none" stroke="#1f1f2b"/><ellipse cx="6" cy="6" rx="2.5" ry="5.5" fill="none" stroke="#1f1f2b"/><path d="M0.5 6 H11.5" stroke="#1f1f2b"/></svg>
          www.brivomatex.example
        </li>
      </ul>
    </div>
    <div class="pillars">
      <span class="pillar-strategy">• STRATEGY</span>
      <span class="pillar-execution">• EXECUTION</span>
      <span class="pillar-results">• RESULTS</span>
    </div>
  </section>

  <section class="card card-back" aria-label="Business card back">
    <div class="back-brand">
      <span class="brand-dot"></span>
      <span class="brand-name">BrivoMatex</span>
    </div>
    <div class="claim">Lantern for the Steady Growth</div>
  </section>
</body>
</html>
```